Sleek and elegant promotional banner/sign for The Belvane Law Firm

We need a design for promotional items like banners, signs, print ads, etc. that includes our firm name - "The Belvane Law Firm" - and what we do. We advise businesses and individuals on legal matters; we represent individuals and businesses in litigation and transactions; we select and create business entities; we solve legal problems for individuals and businesses, etc. PLEASE DO NOT SIMPLY REPEAT THE PREVIOUS SENTENCE ON THE DESIGN. Please create a tag-line or brief description from ours. We need something that describes what we do in concise and creative manner while communicating trust and confidence. The banner must also include our basic contact information: 818.452-7196 (telephone) and belvanelaw.example (website). You may use one or more of the attached images, but needn't use any with the right design. The design should be sleek and modern.

Target Market(s)

wealthy individuals and small business owners, entrepreneurs

Industry/Entity Type

Lawyer

Font styles to use
Sans Serif

Colors
33a6d7
0556a4
33b8a4

Requirements
Must have
• Firm name, contact information, BRIEF description of our services, sleek and elegant.
• Also, the design must be horizontal - not vertical.
Nice to have
• I'd like to use one of the images
Should not have
• Cliches

```html
<!DOCTYPE html>
<html lang="en">
<head>
<meta charset="utf-8">
<title>The Belvane Law Firm – Banner</title>
<link href="https://fonts.googleapis.com/css2?family=Oswald:wght@400;500&family=Montserrat:wght@500&display=swap" rel="stylesheet">
<style>
  :root {
    --stage: #1c1d1f;
    --navy: #0b3f8e;
    --teal: #33b8a4;
    --ink: #141414;
    --white: #ffffff;
    --glass-light: #f3f7fa;
    --glass-mid: #d6e3ee;
    --glass-deep: #b9cde0;
  }
  * { margin: 0; padding: 0; box-sizing: border-box; }
  html, body {
    width: 1200px;
    height: 1000px;
    overflow: hidden;
    background: var(--stage);
  }
  .banner {
    position: absolute;
    left: 50px;
    top: 225px;
    width: 1100px;
    height: 550px;
    overflow: hidden;
    font-family: "Oswald", "Arial Narrow", sans-serif;
  }
  .banner__backdrop {
    position: absolute;
    inset: 0;
    background:
      linear-gradient(120deg, var(--glass-mid) 0%, var(--glass-light) 35%, var(--glass-light) 60%, var(--glass-deep) 100%);
  }
  .brand {
    position: absolute;
    top: 52px;
    left: 0;
    right: 0;
    display: flex;
    justify-content: center;
    align-items: center;
    gap: 16px;
  }
  .brand__mark {
    width: 34px;
    height: 34px;
    background: var(--ink);
  }
  .brand__name {
    font-family: "Oswald", "Arial Narrow", sans-serif;
    font-weight: 400;
    font-size: 44px;
    letter-spacing: 2px;
    color: var(--ink);
    text-transform: uppercase;
  }
  .tagline {
    position: absolute;
    top: 112px;
    left: 0;
    right: 0;
    text-align: center;
  }
  .tagline span {
    display: inline-block;
    font-family: "Montserrat", Arial, sans-serif;
    font-weight: 500;
    font-size: 17px;
    letter-spacing: 1.5px;
    color: var(--ink);
    padding: 5px 6px 6px;
    border-top: 1.5px solid var(--ink);
    border-bottom: 1.5px solid var(--ink);
  }
  .rule {
    position: absolute;
    left: 0;
    right: 0;
    height: 7px;
    background: var(--teal);
  }
  .rule--top { top: 213px; }
  .rule--bottom { top: 392px; }
  .practice-band {
    position: absolute;
    left: 0;
    right: 0;
    top: 224px;
    height: 164px;
    background: var(--navy);
    color: var(--white);
    text-align: center;
  }
  .practice-band__intro {
    margin-top: 10px;
    font-style: italic;
    font-size: 21px;
    font-weight: 400;
    letter-spacing: 0.3px;
  }
  .practice-band__list {
    font-size: 40px;
    font-weight: 400;
    line-height: 58px;
    letter-spacing: 0.3px;
  }
  .practice-band__sep { margin: 0 18px; }
  .contact {
    position: absolute;
    top: 452px;
    left: 0;
    right: 0;
    text-align: center;
    font-size: 30px;
    font-weight: 500;
    color: var(--ink);
  }
  .contact__label,
  .contact__domain { color: var(--navy); }
  .contact__sep { margin: 0 12px; }
</style>
</head>
<body>
  <main class="banner">
    <div class="banner__backdrop" role="img" aria-label="Soft photograph of a glass office tower reflecting blue sky"></div>

    <header class="brand">
      <span class="brand__mark"></span>
      <h1 class="brand__name">The Belvane Law Firm</h1>
    </header>

    <p class="tagline"><span>PROVIDING EXCEPTIONAL RESULTS FOR ITS CLIENTS</span></p>

    <div class="rule rule--top"></div>
    <section class="practice-band">
      <p class="practice-band__intro">EXPERIENCE IN CASES INVOLVING</p>
      <p class="practice-band__list">BUSINESS<span class="practice-band__sep">|</span>CONTRACTS<span class="practice-band__sep">|</span>REAL ESTATE<span class="practice-band__sep">|</span></p>
      <p class="practice-band__list">SHAREHOLDER PARTNERSHIP DISPUTES<span class="practice-band__sep">|</span>ESTATE PLANNING</p>
    </section>
    <div class="rule rule--bottom"></div>

    <p class="contact">
      <span class="contact__label">CONTACT US AT:</span> 818.452-7196<span class="contact__sep">|</span>WWW.<span class="contact__domain">BELVANELAW</span>.EXAMPLE
    </p>
  </main>
</body>
</html>
```